Lena Hartwell Web

Lena Hartwell is a singer/songwriter that has a presence in the market for over 20 years. She currently has a website, lenahartwell.example that needs a major makeover. IT needs to be reorganized to; 1) make it more user friendly; 2) enable multi-languages including; Spanish, French, Russian, Japanese, Chinese and Portuguese; 3) enable purchases online through a storefront of promotional merchandise and music tracks. She has a logo that needs an update, as well as we currently have a business card open on PixelBazaar for input. Working to re-brand, or refresh her brand.

Lena Hartwell is the next Rosa Delmont! She has 5 platinum records, Lumen Award nominations and tours with Harold Prescott globally and is Nora Vandermeer's key backup singer for 12 years.
Updates

Some common questions have come up.  Here is some further input:

1) Colors - No specific color in mind but probably earth tones.  Although at this point we''re completely open.  Mary likes classical style, Russian, French decor.  Paris architecture. Greek, Italian textures, Goddess like symbols from the Roman Empire, or the symbols and pomp of the British monarchy.  One name on tap for the new CD is "Lanterns Over Quiet Water"
2) Example website - I have not found a new one specifically, but what I don''t like about the existing one is it is not easy to navigate.  Needs to be streamlined and easy to navigate with a storefront for merchandise and music downloads.  
3) On Logo - We''re revamping a "Global" merchandise rollout logo.  We''ve also considered possibly modifying the old english "Hartwell" family crest which signifies royalty, but have not explored that too much.  The hexagon yellow logo on her current website, I was thinking of modifying to gold (brushed - or polished?), then taking the LH lettering using a fountain pen type look there the line thickness flows with pressure on the pen, then make the gold look like a pillow, with the letter making an impression into the gold pillow.  This expands to a high quality pin, blinged up broach with diamonds imbedded for example, Global label identity, tee shirts, label tag on fashion clothing etc etc. 
 4) One thing marketing has asked us to build is a routine video blog to reach out to fans in a personal way.  Short clips of daily activity, travel prep for shows, etc. Possibly a signup/fanpage where people get emails sent back whenever anything new is posted, like a video blog, new pics, new events.  A menu to choose what you get updates on. 

Thanks, Dennis

Target Market(s)

1) Fan base in Europe, Asia, Latin America and North America
2) Movie producers seeking soundtracks
3) Private clients seeking an outstanding performer for corporate events

Industry/Entity Type

Singer

Requirements
Must have
• Better organization into smaller pages. Items critical include: 1) music tracks, 2) ClipStream links, 3) photos & Video, 4) storefront to enable online merchandise purchase 5) a way to illustrate her genre from; gospel, to rock, funk, R&B, country,

```html
<!DOCTYPE html>
<html lang="en">
<head>
<meta charset="utf-8">
<title>Lena Hartwell — Official Site</title>
<link href="https://fonts.googleapis.com/css2?family=Arimo:wght@400;700&family=Oswald:wght@300;400;500&family=PT+Serif:wght@400;700&family=Pinyon+Script&family=Raleway:wght@200&display=swap" rel="stylesheet">
<style>
:root{
  --ink:#333a40;
  --muted:#7a7f85;
  --pink:#e0287f;
  --blue:#2a8fc6;
  --link:#2f7fb8;
  --nav-bg:#bfe2e3;
  --ghost:#aab2bc;
  --page-bg:#efefef;
  --card:#ffffff;
  --line:#dcdcdc;
  --gold-hi:#f6d767;
  --gold:#d39a24;
  --gold-lo:#7d4f0c;
  --thumb:#3a1836;
  --rss:#f08a24;
}
*{box-sizing:border-box;margin:0;padding:0}
html,body{width:857px;height:1200px;overflow:hidden;background:#fff}
body{font-family:"Arimo",Arial,sans-serif;color:var(--ink)}
.stage{position:absolute;left:0;top:0;width:800px;height:1120px;transform:scale(1.07125);transform-origin:0 0;overflow:hidden}
.abs{position:absolute}

/* backdrop */
.ghost-name{position:absolute;left:-52px;top:-22px;font-family:"Raleway",sans-serif;font-weight:200;font-size:112px;color:var(--ghost);white-space:nowrap;letter-spacing:-1px;opacity:.85}
.hero-portrait{position:absolute;left:0;top:48px;width:252px;height:860px;background:linear-gradient(180deg,#e9dccd 0%,#f6efe6 30%,#fbf8f4 70%,#ffffff 100%);border-radius:0 0 60px 0}

/* header */
.brand{position:absolute;left:463px;top:3px;width:74px;height:42px;display:flex;align-items:center;justify-content:center;gap:4px}
.brand-dot{width:9px;height:9px;border-radius:50%;background:var(--gold)}
.brand-name{font-family:"PT Serif",serif;font-size:22px;color:var(--gold-lo)}
.langs{position:absolute;left:572px;top:10px;display:flex;gap:12px;font-size:6.5px;color:var(--muted)}
.langs span{display:flex;align-items:center;gap:3px}
.flag{width:8px;height:5px;display:inline-block}
.flag-en{background:linear-gradient(90deg,#1d3b8a 0 40%,#c8102e 40% 60%,#1d3b8a 60%)}
.flag-es{background:linear-gradient(180deg,#c60b1e 0 25%,#ffc400 25% 75%,#c60b1e 75%)}
.flag-fr{background:linear-gradient(90deg,#0055a4 0 33%,#fff 33% 66%,#ef4135 66%)}
.flag-ru{background:linear-gradient(180deg,#fff 0 33%,#0039a6 33% 66%,#d52b1e 66%)}
.search{position:absolute;left:612px;top:30px;width:117px;height:15px;border:1px solid #ccc;border-radius:2px;font-size:6px;color:#999;padding:3px 5px;background:#fff}
.search svg{position:absolute;right:4px;top:3px}

.nav{position:absolute;left:250px;top:55px;width:478px;height:22px;background:var(--nav-bg);display:flex;align-items:center;padding-left:10px;gap:0}
.nav a{font-family:"Oswald",sans-serif;font-weight:400;font-size:10.5px;color:#3b4b52;text-decoration:none;text-transform:uppercase}
.nav a.current{color:var(--pink)}

/* hero */
.hero-frame{position:absolute;left:248px;top:75px;width:486px;height:382px;border-radius:18px;background:radial-gradient(ellipse at 50% 50%,var(--gold-hi) 0%,var(--gold) 55%,var(--gold-lo) 100%)}
.hero-photo{position:absolute;left:300px;top:125px;width:240px;height:282px;background:linear-gradient(160deg,#5d7788 0%,#2b2f36 45%,#b09a8e 100%)}
.hero-title{position:absolute;left:315px;top:305px;background:rgba(20,20,20,.82);color:#fff;font-family:"Oswald",sans-serif;font-weight:400;font-size:31px;line-height:38px;padding:0 7px;letter-spacing:.5px;white-space:nowrap}
.hero-sub{position:absolute;left:315px;top:344px;background:rgba(40,40,40,.75);color:#ddd;font-family:"Oswald",sans-serif;font-weight:300;font-size:10.5px;padding:1px 7px;text-transform:uppercase;white-space:nowrap}
.bio{position:absolute;left:540px;top:125px;width:145px;height:282px;background:linear-gradient(180deg,#cfe9ec 0%,#a8d3d8 100%);padding:12px 8px 0 6px;overflow:hidden}
.bio h2{font-family:"Oswald",sans-serif;font-weight:400;font-size:21px;color:var(--pink);margin-left:22px;letter-spacing:.5px}
.bio p{font-family:"Pinyon Script",cursive;font-size:13px;line-height:17.5px;color:#3d3e3a;margin-top:10px}

/* content area */
.content-bg{position:absolute;left:250px;top:457px;width:478px;height:663px;background:var(--page-bg);box-shadow:0 0 6px rgba(0,0,0,.12)}
.card{position:absolute;background:var(--card);border:1px solid var(--line);box-shadow:0 1px 2px rgba(0,0,0,.06)}
.sec-title{font-family:"PT Serif",serif;font-size:10.5px;text-transform:uppercase;color:#2d3236;letter-spacing:.3px}
.sec-title em{font-style:normal;color:var(--pink)}
.rss{position:absolute;width:9px;height:9px;border-radius:2px;background:var(--rss)}
.blue-cap{font-family:"Arimo",sans-serif;font-weight:700;font-size:6px;color:var(--blue);text-transform:uppercase;line-height:8px}
.thumb{position:absolute;background:radial-gradient(circle at 50% 40%,#6b3a5f 0%,var(--thumb) 70%);border:3px solid #fff;box-shadow:0 0 0 1px #ddd}
.body-text{font-size:6px;line-height:7.5px;color:#555}

/* intro */
.intro{left:270px;top:475px;width:296px;height:146px}
.intro .sec-title{position:absolute;left:6px;top:6px}
.intro-photo{position:absolute;left:7px;top:19px;width:80px;height:106px;background:linear-gradient(170deg,#4a3a3a,#8b6a58 50%,#2c2220)}
.intro-text{position:absolute;left:93px;top:18px;width:196px}
.intro-text .lead{font-weight:700;font-size:7px;color:var(--blue);text-transform:uppercase}
.intro-text .kicker{font-size:6px;color:#666;text-transform:uppercase;margin-bottom:1px}
.intro-text p{margin-bottom:5px}
.pager{position:absolute;left:6px;top:133px;display:flex;gap:10px;font-size:5.5px;color:var(--link);text-transform:uppercase}

/* videos */
.videos{left:270px;top:625px;width:296px;height:216px}
.video-feature{position:absolute;left:6px;top:6px;width:136px;height:184px;background:linear-gradient(180deg,#2e3a42 0%,#6b6660 45%,#3b2a28 100%)}
.video-caption{position:absolute;left:26px;top:140px;width:114px;padding:3px 5px;background:rgba(25,25,25,.8);font-family:"Oswald",sans-serif;font-weight:500;font-size:10px;line-height:12px;color:var(--blue);text-transform:uppercase}
.videos .sec-title{position:absolute;left:148px;top:6px}
.videos .rss{left:280px;top:8px}
.videos .rule{position:absolute;left:148px;top:19px;width:142px;border-top:1px solid var(--line)}
.btn{position:absolute;left:5px;top:198px;padding:2px 5px;background:#e6e6e6;border:1px solid #ccc;border-radius:2px;font-size:5px;color:#555;text-transform:uppercase}

/* photos */
.photos{left:270px;top:845px;width:296px;height:120px}
.photos .sec-title{position:absolute;left:6px;top:5px}
.photos .rss{left:283px;top:6px}
.photos .rule{position:absolute;left:6px;top:18px;width:284px;border-top:1px solid var(--line)}

/* news tabs */
.news{left:270px;top:970px;width:296px;height:93px}
.tabs{position:absolute;left:0;top:0;display:flex;font-family:"PT Serif",serif;font-size:6.5px;text-transform:uppercase;color:#5c7a8c}
.tabs span{padding:3px 4px;border-right:1px solid var(--line);border-bottom:1px solid var(--line)}
.tabs span.active{border-bottom-color:transparent}
.news-item{position:absolute;top:22px;width:70px}
.news-item .body-text{margin:3px 0}
.news-item .more{font-size:5.5px;color:var(--link);text-transform:uppercase}

/* sidebar */
.sidebar{left:570px;top:475px;width:142px;height:590px}
.side-title{position:absolute;left:4px;font-family:"PT Serif",serif;font-size:9.5px;text-transform:uppercase;color:#2d3236;width:132px;border-bottom:1px solid var(--line);padding-bottom:3px}
.merch-list{position:absolute;left:5px;top:22px;list-style:none}
.merch-list li{font-size:6px;line-height:12px;color:var(--pink);text-transform:uppercase;display:flex;align-items:center;gap:4px}
.merch-list li::before{content:"";width:5px;height:5px;border-radius:50%;background:#c9c9c9}
.ad-label{position:absolute;left:4px;top:116px;font-size:4.5px;color:#aaa;text-transform:uppercase}
.ad{position:absolute;left:7px;top:123px;width:130px;height:130px;background:linear-gradient(160deg,#8a6a4a 0%,#c7a27a 40%,#7a2a28 75%,#5a3f2c 100%)}
.event-list{position:absolute;left:4px;top:288px;width:134px;list-style:none}
.event-list li{font-size:5.8px;line-height:6.5px;color:var(--link);text-decoration:underline;border-bottom:1px solid #ececec;padding:2px 0}
.blog-list{position:absolute;left:4px;top:426px;width:134px;list-style:none}
.blog-list li{margin-bottom:2.5px;border-bottom:1px solid #ececec;padding-bottom:1px}
.blog-meta{font-size:4.8px;color:#888}
.blog-meta b{font-weight:400;color:var(--pink);text-decoration:underline}
.blog-link{font-size:5.8px;line-height:6.5px;color:var(--link);text-decoration:underline}

/* footer */
.footer{left:270px;top:1068px;width:442px;height:32px}
.footer-brand{position:absolute;left:16px;top:6px;display:flex;align-items:center;gap:3px}
.footer-brand .brand-dot{width:6px;height:6px;background:#aaa}
.footer-brand .brand-name{font-size:14px;color:#777}
.credit{position:absolute;right:10px;top:12px;font-size:5px;color:#777;text-transform:uppercase}
.credit span{color:var(--pink);text-decoration:underline}
</style>
</head>
<body>
<div class="stage">

  <div class="hero-portrait" role="img" aria-label="Full-length portrait of the singer in a flowing white gown, softly faded into the page"></div>
  <div class="ghost-name" aria-hidden="true">Lena Hartwell</div>

  <header>
    <div class="brand"><span class="brand-dot"></span><span class="brand-name">LH</span></div>
    <div class="langs">
      <span><i class="flag flag-en"></i>English</span>
      <span><i class="flag flag-es"></i>Spanish</span>
      <span><i class="flag flag-fr"></i>French</span>
      <span><i class="flag flag-ru"></i>Russian</span>
    </div>
    <div class="search">What are you looking for?
      <svg width="7" height="7" viewBox="0 0 10 10"><circle cx="4" cy="4" r="3" fill="none" stroke="#999" stroke-width="1.4"/><line x1="6.3" y1="6.3" x2="9.3" y2="9.3" stroke="#999" stroke-width="1.4"/></svg>
    </div>
    <nav class="nav">
      <a class="current" style="width:52px">Home</a>
      <a style="width:50px">Events</a>
      <a style="width:49px">Music</a>
      <a style="width:49px">Video</a>
      <a style="width:62px">Pictures</a>
      <a style="width:51px">About</a>
      <a style="width:74px">Discography</a>
      <a>Contact</a>
    </nav>
  </header>

  <section>
    <div class="hero-frame" role="img" aria-label="Ornate carved gold baroque picture frame"></div>
    <div class="hero-photo" role="img" aria-label="Close-up portrait of the singer with short dark hair and a fur collar"></div>
    <div class="hero-title">LENA HARTWELL</div>
    <div class="hero-sub">Lanterns Over Quiet Water</div>
    <div class="bio">
      <h2>BIOGRAPHY</h2>
      <p>Lena Hartwell is the next Rosa Delmont! She hs 5 platinum records, Lumen Award nominations and tours with Harold Prescott globally and is Nora Vandermeer's key backup singer for 12 years Lena Hartwell is the next Rosa Delmont! She hs 5 platinum records</p>
    </div>
  </section>

  <div class="content-bg"></div>

  <main>
    <article class="card intro">
      <h2 class="sec-title"><em>Lena Hartwell</em> Lanterns Over Quiet Water!</h2>
      <div class="intro-photo" role="img" aria-label="The singer performing on stage with a duet partner"></div>
      <div class="intro-text body-text">
        <div class="lead">Lorem ipsum dolor sit amet</div>
        <div class="kicker">Welcome to my site</div>
        <p>Lorem ipsum dolor sit amet, consectetur adipiscing elit. Pellentesque turpis urna, rhoncus a tempus in, blandit vel nibh. Sed interdum erat eget lacus commodo mattis. Donec ac ante ut dui scelerisque consequat. Phasellus facilisis luctus elit ac sollicitudin. Curabitur pulvinar malesuada accumsan.</p>
        <p>Donec luctus mauris a velit aliquam in volutpat diam viverra. Nulla ipsum magna, pellentesque et imperdiet eget, interdum sed neque.</p>
        <p>Nullam tempor pellentesque pulvinar. Quisque elementum purus vitae urna vulputate molestie. Nam tortor tellus, pulvinar non pellentesque eget, aliquam vel ligula. Curabitur eleifend, diam ac pulvinar porttitor, massa elit lobortis ligula, a blandit nunc nulla vitae mauris. Nullam laoreet lacus ut quam sodales semper.</p>
      </div>
      <div class="pager"><span>Previous news</span><span>All news</span><span>Next news</span></div>
    </article>

    <section class="card videos">
      <div class="video-feature" role="img" aria-label="The singer in a red gown leaning on a bar counter"></div>
      <div class="video-caption">Lorem ipsum dolor sit amet</div>
      <h2 class="sec-title">Latest Videos</h2>
      <span class="rss"></span>
      <div class="rule"></div>
      <div class="thumb" style="left:150px;top:25px;width:66px;height:66px" role="img" aria-label="Video still of the singer on stage"></div>
      <div class="thumb" style="left:225px;top:25px;width:66px;height:66px" role="img" aria-label="Video still of the singer on stage"></div>
      <div class="thumb" style="left:150px;top:112px;width:66px;height:66px" role="img" aria-label="Video still of the singer on stage"></div>
      <div class="thumb" style="left:225px;top:112px;width:66px;height:66px" role="img" aria-label="Video still of the singer on stage"></div>
      <div class="blue-cap abs" style="left:149px;top:94px">Title of the video</div>
      <div class="blue-cap abs" style="left:224px;top:94px">Title of the video</div>
      <div class="blue-cap abs" style="left:149px;top:180px">Title of the video</div>
      <div class="blue-cap abs" style="left:224px;top:180px">Title of the video</div>
      <div class="btn">View all videos</div>
    </section>

    <section class="card photos">
      <h2 class="sec-title">Latest Photos</h2>
      <span class="rss"></span>
      <div class="rule"></div>
      <div class="thumb" style="left:6px;top:27px;width:66px;height:66px" role="img" aria-label="Concert photo of the singer"></div>
      <div class="thumb" style="left:79px;top:27px;width:66px;height:66px" role="img" aria-label="Concert photo of the singer"></div>
      <div class="thumb" style="left:152px;top:27px;width:66px;height:66px" role="img" aria-label="Concert photo of the singer"></div>
      <div class="thumb" style="left:225px;top:27px;width:66px;height:66px" role="img" aria-label="Concert photo of the singer"></div>
      <div class="blue-cap abs" style="left:6px;top:97px;width:66px">Lorem ipsum dolor sitamet</div>
      <div class="blue-cap abs" style="left:79px;top:97px;width:66px">Pellentesque turpisurna</div>
      <div class="blue-cap abs" style="left:152px;top:97px;width:66px">Phasellus facilisisluctus</div>
      <div class="blue-cap abs" style="left:224px;top:97px;width:66px">Uisque elementumpurus vitae urn</div>
    </section>

    <section class="card news">
      <div class="tabs"><span class="active">Latest News</span><span>Tours</span><span>Shows</span><span>Press</span><span>Music</span></div>
      <div class="thumb" style="left:6px;top:22px;width:66px;height:66px" role="img" aria-label="News photo of the singer on stage"></div>
      <div class="news-item" style="left:76px">
        <div class="blue-cap">Lorem ipsum dolor sitamet</div>
        <div class="body-text">Donec luctus mauris a velit aliquam in volutpat diam viverra.Nulla ipsum magna.</div>
        <div class="more">Read full story</div>
      </div>
      <div class="thumb" style="left:151px;top:22px;width:66px;height:66px" role="img" aria-label="News photo of the singer on stage"></div>
      <div class="news-item" style="left:220px">
        <div class="blue-cap">Uisque elementumpurus vitae urn</div>
        <div class="body-text">Donec luctus mauris a velit aliquam in volutpat diam viverra.Nulla ipsum magna.</div>
        <div class="more">Read full story</div>
      </div>
    </section>
  </main>

  <aside class="card sidebar">
    <h2 class="side-title" style="top:5px">Marchandise</h2>
    <ul class="merch-list">
      <li>Videos</li><li>Music tracks</li><li>Photos</li><li>Favourites</li><li>Other items</li><li>Other items</li><li>Other items</li>
    </ul>
    <div class="ad-label">Advertising</div>
    <div class="ad" role="img" aria-label="Advertisement photo of the singer in a red gown in a wood-panelled room"></div>

    <h2 class="side-title" style="top:267px">Latest Events</h2>
    <ul class="event-list">
      <li>Lorem ipsum dolor sit amet, consectetur adipiscing elit.</li>
      <li>Lorem ipsum dolor sit amet</li>
      <li>Lorem ipsum dolor sit amet</li>
      <li>Lorem ipsum dolor sit amet</li>
      <li>Lorem ipsum dolor sit amet</li>
      <li>Lorem ipsum dolor sit amet</li>
      <li>Lorem ipsum dolor sit amet</li>
      <li>Lorem ipsum dolor sit amet</li>
      <li>Lorem ipsum dolor sit amet</li>
    </ul>

    <h2 class="side-title" style="top:405px">Blog Roll</h2>
    <ul class="blog-list">
      <li><div class="blog-meta">21.05.2013 | posted by <b>admin</b></div><div class="blog-link">Lorem ipsum dolor sit amet, consectetur adipiscing elit.</div></li>
      <li><div class="blog-meta">21.05.2013 | posted by <b>admin</b></div><div class="blog-link">Nulla ipsum magna pellentesque et imperdiet eget, interdum sed neque</div></li>
      <li><div class="blog-meta">21.05.2013 | posted by <b>admin</b></div><div class="blog-link">Consectetur adipiscing elit pellentesque turpis urna tempus.</div></li>
      <li><div class="blog-meta">21.05.2013 | posted by <b>admin</b></div><div class="blog-link">Curabitu eleifend,, diam ac pulvinar porttitor, massa elit lobortis ligula a blandit</div></li>
      <li><div class="blog-meta">21.05.2013 | posted by <b>admin</b></div><div class="blog-link">Lorem ipsum dolor sit amet, consectetur adipiscing elit.</div></li>
      <li><div class="blog-meta">21.05.2013 | posted by <b>admin</b></div><div class="blog-link">Lorem ipsum dolor sit amet, consectetur adipiscing elit.</div></li>
    </ul>
  </aside>

  <footer class="card footer">
    <div class="footer-brand"><span class="brand-dot"></span><span class="brand-name">LH</span></div>
    <div class="credit">© <span>sitename.com</span>, design by designers name</div>
  </footer>

</div>
</body>
</html>
```